Meadow Crate Co came about when a life change having to do with my health became an issue and I had to change my diet. We’re a homeschool family and learned a more simplistic way to eat and live out our day to day. We’re ready to share how we eat. Included are attachments to give a visual to the concepts in mind. The first attachment is the logo the second is basically the main idea of the company referencing to getting to the roots of nutrition and juicing. The roots design CONCEPT would be incorporated onto the bottle label. The third attachment is representing the clear stickers we’d like to have on bottles. The 4th and Last are the bottle design we’re looking to use. We’d like tall cylinder bottles.

Label must haves :
meadow crate co logo and the quote know your roots
The roots design
MeadowCrateCo.example

```html
<!DOCTYPE html>
<html lang="en">
<head>
<meta charset="utf-8">
<title>Meadow Crate Co — Know Your Roots bottle labels</title>
<link href="https://fonts.googleapis.com/css2?family=Open+Sans:wght@400;600&family=Roboto+Condensed:wght@700&display=swap" rel="stylesheet">
<style>
  :root {
    --page: #ffffff;
    --juice-light: #8a9a2c;
    --juice-mid: #7f8f28;
    --juice-dark: #5b6b1f;
    --leaf-green: #a6f59a;
    --sun-yellow: #f2e521;
    --logo-green: #1f8a34;
    --stone-grey: #b3b3b3;
    --ink: #111111;
    --panel: #3a3a3a;
    --panel-gold: #4a4535;
    --panel-silver: #4a4a4a;
    --url-dark: #2a2a1c;
    --url-light: #f4f4ec;
  }
  * { box-sizing: border-box; margin: 0; padding: 0; }
  html, body { width: 1113px; height: 1200px; overflow: hidden; background: var(--page); }
  .canvas { position: relative; width: 1113px; height: 1200px; }

  .label {
    position: absolute; top: 300px; width: 360px; height: 700px;
    border-radius: 28px;
    background: linear-gradient(90deg, var(--juice-light) 0%, var(--juice-mid) 55%, var(--juice-dark) 100%);
  }
  .label--colour { left: 110px; }
  .label--mono { left: 643px; }

  .brand-mark {
    position: absolute; left: 105px; top: 60px; width: 150px; height: 150px;
    border-radius: 50%;
    display: flex; align-items: center; justify-content: center; text-align: center;
    font-family: "Roboto Condensed", sans-serif; font-weight: 700;
    font-size: 30px; line-height: 1.02;
  }
  .label--colour .brand-mark { background: var(--sun-yellow); color: var(--logo-green); }
  .label--mono .brand-mark { background: var(--stone-grey); color: var(--ink); }

  .tagline {
    position: absolute; left: 0; top: 262px; width: 100%;
    font-family: "Roboto Condensed", sans-serif; font-weight: 700;
    font-size: 40px; line-height: 1.02; letter-spacing: 0.5px;
  }
  .tagline__know { display: block; padding-left: 58px; }
  .tagline__rest { display: block; padding-left: 88px; }
  .tagline__roots { margin-left: 12px; }
  .label--colour .tagline__know,
  .label--colour .tagline__roots { color: var(--leaf-green); }
  .label--colour .tagline__your { color: var(--ink); }
  .label--mono .tagline { color: var(--url-light); }

  .roots-art {
    position: absolute; left: 80px; top: 380px; width: 200px; height: 210px;
  }
  .label--colour .roots-art { background: radial-gradient(ellipse at 50% 60%, var(--panel-gold) 0%, var(--panel) 70%); }
  .label--mono .roots-art { background: radial-gradient(ellipse at 50% 60%, var(--panel-silver) 0%, var(--panel) 70%); }

  .site-url {
    position: absolute; left: 0; top: 628px; width: 100%; text-align: center;
    font-family: "Open Sans", sans-serif; font-weight: 600; font-size: 15px; letter-spacing: 1px;
  }
  .label--colour .site-url { color: var(--url-dark); }
  .label--mono .site-url { color: var(--url-light); }
</style>
</head>
<body>
<main class="canvas">

  <section class="label label--colour">
    <div class="brand-mark">Meadow<br>Crate<br>Co</div>
    <h2 class="tagline">
      <span class="tagline__know">KNOW</span>
      <span class="tagline__rest"><span class="tagline__your">YOUR</span><span class="tagline__roots">ROOTS</span></span>
    </h2>
    <div class="roots-art" role="img" aria-label="Illustration of a sprout whose gold roots spread like a pair of lungs on a dark panel"></div>
    <p class="site-url">MeadowCrateCo.example</p>
  </section>

  <section class="label label--mono">
    <div class="brand-mark">Meadow<br>Crate<br>Co</div>
    <h2 class="tagline">
      <span class="tagline__know">KNOW</span>
      <span class="tagline__rest"><span class="tagline__your">YOUR</span><span class="tagline__roots">ROOTS</span></span>
    </h2>
    <div class="roots-art" role="img" aria-label="Illustration of a sprout whose white roots spread like a pair of lungs on a dark panel"></div>
    <p class="site-url">MeadowCrateCo.example</p>
  </section>

</main>
</body>
</html>
```